Bref créative
Stationery, etc. for a tax preparation company
looking for creative designs!
Professional
Gordon Pallister
4829 Brevard Court, Suite 100
Edina, Minnesota 55812
gordy@gordyvalmor.com
www.gptaxhelpers.com
We'd like something a little bit creative that stands out.
We'd like the back of the business card to be a lighter color so someone could write on it, if necessary.

```html
<!DOCTYPE html>
<html lang="en">
<head>
<meta charset="utf-8">
<title>GP Tax Helpers – Business Card</title>
<link rel="stylesheet" href="https://fonts.googleapis.com/css2?family=Cinzel:wght@400;600&family=Open+Sans:wght@400;600&display=swap">
<style>
  :root {
    --page-bg: #e9e7ec;
    --purple: #6a3c7f;
    --purple-deep: #4f2a62;
    --purple-light: #8a5ca0;
    --lavender: #d9c9e4;
    --white: #ffffff;
    --card-white: #f7f7f8;
    --grey: #8c8c90;
    --grey-dark: #55555a;
  }
  * { margin: 0; padding: 0; box-sizing: border-box; }
  html, body {
    width: 1200px; height: 864px; overflow: hidden;
    background: var(--page-bg);
  }
  .canvas {
    position: relative; width: 1200px; height: 864px;
  }
  .card {
    position: absolute; left: 280px; width: 640px; height: 366px;
    border-radius: 18px; overflow: hidden;
    box-shadow: 0 10px 28px rgba(40, 20, 50, 0.22);
  }

  /* Back of card */
  .card-back {
    top: 46px;
    background: radial-gradient(ellipse at 50% 45%, var(--purple-light) 0%, var(--purple) 55%, var(--purple-deep) 100%);
  }
  .back-mark {
    position: absolute; left: 0; right: 0; top: 138px;
    display: flex; align-items: center; justify-content: center; gap: 14px;
  }
  .back-mark .mark-dot {
    width: 34px; height: 34px; border-radius: 50%; background: var(--lavender);
  }
  .back-mark .mark-name {
    font-family: "Cinzel", serif; font-weight: 600; font-size: 40px;
    color: var(--lavender); letter-spacing: 1px;
  }
  .back-web {
    position: absolute; left: 34px; top: 183px;
    transform: translate(-50%, -50%) rotate(-90deg);
    font-family: "Open Sans", sans-serif; font-size: 12px; letter-spacing: 4px;
    color: var(--lavender); text-transform: uppercase; white-space: nowrap;
  }

  /* Front of card */
  .card-front {
    top: 452px;
    background: linear-gradient(135deg, var(--white) 0%, var(--card-white) 60%, #e6e6e9 100%);
  }
  .front-swoosh { position: absolute; inset: 0; }
  .contact-list {
    position: absolute; right: 20px; top: 20px; list-style: none;
    font-family: "Open Sans", sans-serif; font-size: 10.5px; color: var(--white);
  }
  .contact-list li {
    display: flex; align-items: center; justify-content: flex-end; gap: 8px;
    height: 19px; white-space: nowrap;
  }
  .contact-list .icon {
    width: 10px; height: 10px; border-radius: 50%; background: var(--white);
    flex: none;
  }
  .front-brand {
    position: absolute; left: 36px; top: 222px;
    display: flex; align-items: center; gap: 12px;
  }
  .front-brand .mark-dot {
    width: 26px; height: 26px; border-radius: 50%; background: var(--purple);
  }
  .front-brand .mark-name {
    font-family: "Cinzel", serif; font-weight: 600; font-size: 30px;
    color: var(--purple);
  }
  .front-rule {
    position: absolute; left: 36px; top: 272px; width: 250px; height: 2px;
    background: var(--grey);
  }
  .holder-name {
    position: absolute; left: 36px; top: 284px;
    font-family: "Cinzel", serif; font-size: 15px; letter-spacing: 1.5px;
    color: var(--grey-dark); text-transform: uppercase;
  }
</style>
</head>
<body>
<main class="canvas">

  <section class="card card-back" aria-label="Business card back">
    <div class="back-mark">
      <span class="mark-dot"></span>
      <span class="mark-name">GP Tax Helpers</span>
    </div>
    <p class="back-web">www.gptaxhelpers.com</p>
  </section>

  <section class="card card-front" aria-label="Business card front">
    <svg class="front-swoosh" width="640" height="366" viewBox="0 0 640 366" aria-hidden="true">
      <path d="M265 0 C415 60 500 200 515 366" fill="none" stroke="var(--grey)" stroke-width="6"/>
      <path d="M290 0 C440 50 525 190 545 366 L640 366 L640 0 Z" fill="var(--purple)"/>
    </svg>
    <ul class="contact-list">
      <li>4829 Brevard Court, Suite 100<span class="icon"></span></li>
      <li>Edina, Minnesota 55812<span class="icon"></span></li>
      <li>(612) 555-0148<span class="icon"></span></li>
      <li>(612) 555-0193<span class="icon"></span></li>
      <li>gordy@gordyvalmor.com<span class="icon"></span></li>
      <li>www.gptaxhelpers.com<span class="icon"></span></li>
    </ul>
    <div class="front-brand">
      <span class="mark-dot"></span>
      <span class="mark-name">GP Tax Helpers</span>
    </div>
    <div class="front-rule"></div>
    <p class="holder-name">Gordon Pallister</p>
  </section>

</main>
</body>
</html>
```